Business Card Design

My business is writing crime novels to entertain readers. I write legal thrillers and mysteries. I need a card for publishers, agents, other authors, and media.

Industry/Entity Type

Legal

Contact Information for Business Card

Paul Ostrander
www.ostranderthrillers.example
paulbostrander@mailbox.example
0064 27 5139427

```html
<!DOCTYPE html>
<html lang="en">
<head>
<meta charset="utf-8">
<title>Paul Ostrander — Business Card</title>
<link rel="stylesheet" href="https://fonts.googleapis.com/css2?family=Oxygen:wght@400&family=Marcellus+SC&family=Open+Sans:wght@400&display=swap">
<style>
  :root {
    --page-bg: #d9d9d9;
    --card-bg: #ffffff;
    --accent-red: #a3201f;
    --portrait-grey: #8c8c8c;
    --portrait-dark: #3a3a3a;
    --ink: #222222;
  }
  * { margin: 0; padding: 0; box-sizing: border-box; }
  html, body {
    width: 1200px;
    height: 873px;
    overflow: hidden;
    background: var(--page-bg);
  }
  .canvas {
    position: relative;
    width: 1200px;
    height: 873px;
  }
  .business-card {
    position: absolute;
    left: 75px;
    top: 136px;
    width: 1050px;
    height: 600px;
    background: var(--card-bg);
    box-shadow: 0 6px 24px rgba(0,0,0,0.18);
    overflow: hidden;
  }
  .portrait-panel {
    position: absolute;
    left: 0;
    top: 0;
    width: 560px;
    height: 600px;
  }
  .card-details {
    position: absolute;
    left: 560px;
    top: 0;
    width: 490px;
    height: 600px;
    padding: 80px 36px 0 10px;
  }
  .author-name {
    font-family: "Oxygen", sans-serif;
    font-weight: 400;
    font-size: 52px;
    color: var(--accent-red);
    text-align: right;
    line-height: 1.1;
    letter-spacing: 1px;
    white-space: nowrap;
  }
  .genre-tagline {
    margin-top: 34px;
    font-family: "Marcellus SC", serif;
    font-size: 25px;
    color: var(--ink);
    text-align: center;
    line-height: 1.35;
  }
  .contact-list {
    list-style: none;
    margin-top: 40px;
    margin-left: 14px;
    font-family: "Open Sans", sans-serif;
    font-size: 23px;
    color: var(--ink);
  }
  .contact-item {
    display: flex;
    align-items: center;
    gap: 12px;
    line-height: 1.6;
    white-space: nowrap;
  }
  .contact-icon {
    width: 22px;
    height: 22px;
    flex: none;
  }
</style>
</head>
<body>
<main class="canvas">
  <article class="business-card">
    <svg class="portrait-panel" viewBox="0 0 560 600" width="560" height="600">
      <defs>
        <linearGradient id="portrait-tone" x1="0" y1="0" x2="0" y2="1">
          <stop offset="0" stop-color="var(--portrait-grey)"/>
          <stop offset="0.6" stop-color="#7a7a7a"/>
          <stop offset="1" stop-color="var(--portrait-dark)"/>
        </linearGradient>
      </defs>
      <polygon points="0,0 420,0 540,300 420,600 0,600" fill="url(#portrait-tone)" role="img" aria-label="Author portrait photograph: man in glasses, white shirt and dark leather jacket on a grey backdrop"/>
      <polyline class="accent-border" points="420,0 540,300 420,600" fill="none" stroke="var(--accent-red)" stroke-width="9"/>
    </svg>

    <section class="card-details">
      <h1 class="author-name">Paul Ostrander</h1>
      <p class="genre-tagline">Legal<br>Thrillers and Mysteries<br>Writing</p>
      <ul class="contact-list">
        <li class="contact-item">
          <svg class="contact-icon" viewBox="0 0 24 24" aria-hidden="true">
            <rect x="6" y="1" width="12" height="22" rx="2.5" fill="var(--accent-red)"/>
            <rect x="8" y="4" width="8" height="13" fill="#ffffff"/>
            <circle cx="12" cy="20" r="1.3" fill="#ffffff"/>
          </svg>
          <span>0064 27 5139427</span>
        </li>
        <li class="contact-item">
          <svg class="contact-icon" viewBox="0 0 24 24" aria-hidden="true">
            <rect x="1" y="5" width="22" height="15" rx="1.5" fill="var(--accent-red)"/>
            <polyline points="2,6 12,14 22,6" fill="none" stroke="#ffffff" stroke-width="1.8"/>
          </svg>
          <span>paulbostrander@mailbox.example</span>
        </li>
        <li class="contact-item">
          <svg class="contact-icon" viewBox="0 0 24 24" aria-hidden="true">
            <circle cx="12" cy="12" r="11" fill="var(--accent-red)"/>
            <g fill="none" stroke="#ffffff" stroke-width="1.4">
              <ellipse cx="12" cy="12" rx="4.5" ry="10"/>
              <line x1="2" y1="12" x2="22" y2="12"/>
              <line x1="12" y1="2" x2="12" y2="22"/>
              <path d="M4 7 H20 M4 17 H20"/>
            </g>
          </svg>
          <span>www.ostranderthrillers.example</span>
        </li>
      </ul>
    </section>
  </article>
</main>
</body>
</html>
```